Bref créative
Harbor Crest - Complete Printing Package
Business Cards, Stationary, Envelopes
Professional
Tomas Lendrakis
Registered Migration Agent
PO Box 5871
Canberra ACT 2600
tomas@harborcrest.com.au
www.harborcrest.com.au
Harbor Crest is company that provides migration services to people seeking to apply for a visa to come to Australia.
We would like a business card that stands out, something that resembles an Australian passport or an Australian Visa.
maybe the back of the business card to look like the front cover of a passport.
Harbor Crest - Company Logo (please use second blue color - PANTONE 273 C)
Agent Number Option 1 charcoal color - please display this on the business card somewhere.
Agent Number Option 2 sand color - please display this on the business card somewhere.
GAF Member Option 1 Black - please display this on the business card somewhere.
GAF Member Option 2 Blue - please display this on the business card somewhere.
GAF Member Option 3 Reverse Blue - please display this on the business card somewhere.

```html
<!DOCTYPE html>
<html lang="en">
<head>
<meta charset="utf-8">
<title>HarborCrest – Business Cards</title>
<link rel="stylesheet" href="https://fonts.googleapis.com/css2?family=PT+Serif:ital,wght@0,400;0,700;1,700&display=swap">
<style>
  :root {
    --brand-blue: #1f6aa5;
    --brand-blue-soft: #d9e8f4;
    --ink: #3a3a3a;
    --ink-muted: #6b6b6b;
    --card-white: #ffffff;
    --backdrop: #ece9e4;
  }
  * { margin: 0; padding: 0; box-sizing: border-box; }
  html, body { width: 1200px; height: 852px; overflow: hidden; }
  body {
    background: var(--backdrop);
    font-family: "PT Serif", Georgia, serif;
    color: var(--ink);
    position: relative;
  }
  .card {
    position: absolute;
    width: 540px;
    height: 310px;
    background: var(--card-white);
    border-radius: 22px;
    overflow: hidden;
    box-shadow: 0 6px 18px rgba(0,0,0,0.18);
  }
  .card--classic { left: 40px; top: 271px; }
  .card--icon-band { left: 620px; top: 271px; }

  .band { position: absolute; top: 0; bottom: 0; background: var(--brand-blue); }
  .card--classic .band { left: 62px; width: 50px; }
  .card--icon-band .band { left: 42px; width: 54px; }

  .logo-mark {
    position: absolute;
    width: 58px; height: 58px;
    border-radius: 50%;
    background: var(--card-white);
    border: 5px solid var(--brand-blue);
  }
  .card--classic .logo-mark { left: 58px; top: 58px; }
  .card--icon-band .logo-mark { left: 40px; top: 44px; }

  .brand-name {
    position: absolute;
    font-weight: 700;
    font-size: 31px;
    color: var(--brand-blue);
    letter-spacing: 0.5px;
  }
  .card--classic .brand-name { left: 128px; top: 66px; }
  .card--icon-band .brand-name { left: 112px; top: 52px; }

  .tagline {
    position: absolute;
    display: flex; align-items: center; gap: 8px;
    font-size: 11px;
    letter-spacing: 1.6px;
    text-transform: uppercase;
    color: var(--brand-blue);
  }
  .tagline::before, .tagline::after {
    content: ""; height: 1px; width: 28px; background: var(--brand-blue);
  }
  .card--classic .tagline { left: 132px; top: 110px; }
  .card--icon-band .tagline { left: 116px; top: 96px; }

  .watermark {
    position: absolute;
    width: 96px; height: 96px;
    border-radius: 50%;
    background: var(--brand-blue-soft);
    opacity: 0.7;
  }
  .card--classic .watermark { right: 38px; top: 126px; }
  .card--icon-band .watermark { right: 20px; top: 140px; }

  .agent {
    position: absolute;
    right: 30px;
    text-align: right;
  }
  .card--classic .agent { top: 148px; }
  .card--icon-band .agent { top: 158px; }
  .agent-name { font-style: italic; font-weight: 700; font-size: 16px; color: var(--brand-blue); }
  .agent-role { font-size: 13px; color: var(--ink-muted); margin-top: 2px; }

  .contact { position: absolute; font-size: 12.5px; line-height: 1.45; color: var(--ink); }
  .card--classic .contact { left: 132px; top: 200px; }
  .card--icon-band .contact { left: 116px; top: 184px; }
  .contact .address { margin-bottom: 6px; }
  .contact-line { display: flex; align-items: center; gap: 7px; height: 19px; }
  .contact-line svg { width: 11px; height: 11px; fill: var(--brand-blue); }
  .card--icon-band .contact-line { height: 22px; }

  .band-icons {
    position: absolute; left: 42px; width: 54px; top: 188px;
    display: flex; flex-direction: column; align-items: center;
  }
  .band-icons svg { width: 12px; height: 12px; fill: var(--card-white); }
  .band-icons .slot { height: 22px; display: flex; align-items: center; }
  .band-icons .slot--home { height: 44px; }
</style>
</head>
<body>

  <!-- Card A: plain band with inline contact icons -->
  <section class="card card--classic">
    <div class="band"></div>
    <div class="logo-mark"></div>
    <div class="brand-name">HarborCrest</div>
    <div class="tagline">Migration Services</div>
    <div class="watermark"></div>
    <div class="agent">
      <div class="agent-name">Tomas Lendrakis</div>
      <div class="agent-role">Registered Migration Agent</div>
    </div>
    <div class="contact">
      <div class="address">PO Box 5871<br>Canberra ACT 2600</div>
      <div class="contact-line">
        <svg viewBox="0 0 12 12"><rect x="3" y="0.5" width="6" height="11" rx="1.2"/></svg>
        +61 (0) 455 208 931
      </div>
      <div class="contact-line">
        <svg viewBox="0 0 12 12"><circle cx="6" cy="6" r="5.5"/></svg>
        tomas@harborcrest.com.au
      </div>
      <div class="contact-line">
        <svg viewBox="0 0 12 12"><circle cx="6" cy="6" r="5.5"/></svg>
        www.harborcrest.com.au
      </div>
    </div>
  </section>

  <!-- Card B: icons set inside the band -->
  <section class="card card--icon-band">
    <div class="band"></div>
    <div class="logo-mark"></div>
    <div class="brand-name">HarborCrest</div>
    <div class="tagline">Migration Services</div>
    <div class="watermark"></div>
    <div class="agent">
      <div class="agent-name">Tomas Lendrakis</div>
      <div class="agent-role">Registered Migration Agent</div>
    </div>
    <div class="band-icons">
      <div class="slot slot--home">
        <svg viewBox="0 0 12 12"><path d="M6 0.8 L11.5 6 H9.8 V11.2 H7.2 V8 H4.8 V11.2 H2.2 V6 H0.5 Z"/></svg>
      </div>
      <div class="slot">
        <svg viewBox="0 0 12 12"><rect x="3" y="0.5" width="6" height="11" rx="1.2"/></svg>
      </div>
      <div class="slot">
        <svg viewBox="0 0 12 12"><circle cx="6" cy="6" r="5.5"/></svg>
      </div>
      <div class="slot">
        <svg viewBox="0 0 12 12"><circle cx="6" cy="6" r="5.5"/></svg>
      </div>
    </div>
    <div class="contact">
      <div class="address">PO Box 5871<br>Canberra ACT 2600</div>
      <div class="contact-line">+61 (0) 455 208 931</div>
      <div class="contact-line">tomas@harborcrest.com.au</div>
      <div class="contact-line">www.harborcrest.com.au</div>
    </div>
  </section>

</body>
</html>
```